Business Reporting Graph Illustration

I'm looking for a graphic design to created an illustration of a line chart I have two sample charts that I'd like elements of each combined together to create the project. Below is a link to learn more about this project. This should be designed using any product of the Adobe Suite.
Color Scheme is included within the below link. This will require 2 - 3 rounds of design before final completion.

https://www.plonvadesk.com/file/QWT8HbxuLeMRa302KD5Vpt/Graphic-Design-Project

```html
<!DOCTYPE html>
<html lang="en">
<head>
<meta charset="utf-8">
<title>TV Ad Response Charts</title>
<link rel="stylesheet" href="https://fonts.googleapis.com/css2?family=Open+Sans:wght@400;700&display=swap">
<style>
  :root {
    --page: #ffffff;
    --panel: #001641;
    --signal: #f9b21b;
    --marker: #c8281e;
    --axis: #6e7891;
    --axis-label: #8b93a8;
  }
  html, body {
    margin: 0;
    width: 1200px;
    height: 1191px;
    overflow: hidden;
    background: var(--page);
  }
  .report {
    display: block;
    width: 1200px;
    height: 1191px;
    font-family: "Open Sans", sans-serif;
  }
  .panel { fill: var(--panel); }
  .trend-line { fill: none; stroke: var(--signal); stroke-width: 2; stroke-linejoin: miter; }
  .ad-marker { stroke: var(--marker); stroke-width: 2; }
  .ad-icon { fill: var(--signal); }
  .ad-label { fill: var(--signal); font-size: 9px; font-weight: 700; text-anchor: middle; }
  .axis-line { stroke: var(--axis); stroke-width: 1.2; }
  .axis-title { fill: var(--axis-label); font-size: 12px; }
  .tick-label { fill: var(--axis-label); font-size: 9px; text-anchor: middle; }
</style>
</head>
<body>
<svg class="report" viewBox="0 0 920 913" preserveAspectRatio="none" role="img" aria-label="Two line charts of site traffic spiking after TV ads">
  <defs>
    <linearGradient id="fill-top" gradientUnits="userSpaceOnUse" x1="0" y1="75" x2="0" y2="362">
      <stop offset="0" stop-color="#f9b21b"/>
      <stop offset="1" stop-color="#001641"/>
    </linearGradient>
    <linearGradient id="fill-bottom" gradientUnits="userSpaceOnUse" x1="0" y1="543" x2="0" y2="829">
      <stop offset="0" stop-color="#f9b21b"/>
      <stop offset="1" stop-color="#001641"/>
    </linearGradient>
    <g id="ticks">
      <line class="axis-line" x1="133" y1="0" x2="881" y2="0"/>
      <path class="axis-line" d="M133-6v12M201-4v8M269-4v8M337-4v8M405-4v8M473-4v8M541-4v8M609-4v8M677-4v8M745-4v8M813-4v8M881-6v12"/>
    </g>
  </defs>

  <!-- Chart one -->
  <g class="chart chart-weekday">
    <rect class="panel" x="22" y="15" width="875" height="403"/>
    <polygon fill="url(#fill-top)" points="133,362 133,328 150,328 157,341 180,334 193,348 211,341 223,345 245,331 252,333 270,320 286,330 304,324 349,291 372,75 381,285 398,288 406,304 423,302 431,329 458,318 475,198 489,316 506,303 515,337 530,329 542,100 567,278 581,285 580,304 603,319 615,335 648,341 676,333 678,350 714,336 740,348 777,330 805,352 859,343 877,352 877,362"/>
    <polyline class="trend-line" points="133,328 150,328 157,341 180,334 193,348 211,341 223,345 245,331 252,333 270,320 286,330 304,324 349,291 372,75 381,285 398,288 406,304 423,302 431,329 458,318 475,198 489,316 506,303 515,337 530,329 542,100 567,278 581,285 580,304 603,319 615,335 648,341 676,333 678,350 714,336 740,348 777,330 805,352 859,343 877,352"/>
    <use href="#ticks" y="371"/>
    <text class="axis-title" x="41" y="380">MINUTES</text>
    <g class="tick-labels">
      <text class="tick-label" x="199" y="404">0</text>
      <text class="tick-label" x="267" y="404">2</text>
      <text class="tick-label" x="335" y="404">4</text>
      <text class="tick-label" x="404" y="404">6</text>
      <text class="tick-label" x="467" y="404">8</text>
      <text class="tick-label" x="538" y="404">10</text>
      <text class="tick-label" x="606" y="404">12</text>
      <text class="tick-label" x="675" y="404">14</text>
      <text class="tick-label" x="743" y="404">16</text>
      <text class="tick-label" x="811" y="404">18</text>
      <text class="tick-label" x="879" y="404">20</text>
    </g>
    <line class="ad-marker" x1="301" y1="108" x2="301" y2="390"/>
    <path class="ad-icon" d="M295 63l12 7-12 7z"/>
    <text class="ad-label" x="299" y="93">TV AD</text>
    <line class="ad-marker" x1="436" y1="231" x2="436" y2="390"/>
    <path class="ad-icon" d="M430 186l12 7-12 7z"/>
    <text class="ad-label" x="434" y="216">TV AD</text>
    <line class="ad-marker" x1="512" y1="108" x2="512" y2="390"/>
    <path class="ad-icon" d="M506 63l12 7-12 7z"/>
    <text class="ad-label" x="510" y="93">TV AD</text>
  </g>

  <!-- Chart two -->
  <g class="chart chart-weekend">
    <rect class="panel" x="22" y="484" width="875" height="402"/>
    <polygon fill="url(#fill-bottom)" points="133,829 133,797 150,797 156,810 177,803 190,817 205,810 217,814 237,800 245,802 261,789 273,799 290,792 332,758 351,543 360,753 375,757 384,773 399,771 413,782 443,788 467,803 492,785 521,778 537,660 549,722 562,740 568,755 583,771 598,806 615,794 632,806 656,799 671,587 690,745 705,750 703,773 722,786 744,796 767,782 790,808 811,799 823,778 852,802 881,800 881,829"/>
    <polyline class="trend-line" points="133,797 150,797 156,810 177,803 190,817 205,810 217,814 237,800 245,802 261,789 273,799 290,792 332,758 351,543 360,753 375,757 384,773 399,771 413,782 443,788 467,803 492,785 521,778 537,660 549,722 562,740 568,755 583,771 598,806 615,794 632,806 656,799 671,587 690,745 705,750 703,773 722,786 744,796 767,782 790,808 811,799 823,778 852,802 881,800"/>
    <use href="#ticks" y="838"/>
    <text class="axis-title" x="41" y="847">MINUTES</text>
    <g class="tick-labels">
      <text class="tick-label" x="201" y="873">3</text>
      <text class="tick-label" x="269" y="873">4</text>
      <text class="tick-label" x="337" y="873">5</text>
      <text class="tick-label" x="405" y="873">6</text>
      <text class="tick-label" x="471" y="873">7</text>
      <text class="tick-label" x="539" y="873">8</text>
      <text class="tick-label" x="607" y="873">9</text>
      <text class="tick-label" x="675" y="873">10</text>
      <text class="tick-label" x="743" y="873">11</text>
      <text class="tick-label" x="811" y="873">12</text>
      <text class="tick-label" x="879" y="873">13</text>
    </g>
    <line class="ad-marker" x1="288" y1="582" x2="288" y2="863"/>
    <path class="ad-icon" d="M282 537l12 7-12 7z"/>
    <text class="ad-label" x="286" y="567">TV AD</text>
    <line class="ad-marker" x1="502" y1="705" x2="502" y2="863"/>
    <path class="ad-icon" d="M496 660l12 7-12 7z"/>
    <text class="ad-label" x="500" y="690">TV AD</text>
    <line class="ad-marker" x1="636" y1="582" x2="636" y2="863"/>
    <path class="ad-icon" d="M630 537l12 7-12 7z"/>
    <text class="ad-label" x="634" y="567">TV AD</text>
  </g>
</svg>
</body>
</html>
```